Entertainer/Dancer Business Cards

Corwin Latimer is an up and coming entertainer from Baltimore, Maryland currently relocating to Los Angeles, California for a dance opportunity at the renowned Marnie Holt Movement Loft.
This young man needs to promote himself and his skills in a populous and competitive city.
Hopefully, this card will set him apart from the tons of entertainers in L.A.
It will passed out to fellow entertainers, agents, and random people looking for talent.

I have uploaded an image of the dancer, it is not necessary to use this image; however it is in PSD format if one should decide to incorporate it somehow and would like to make changes.

Industry/Entity Type

Business

Contact Information for Business Card

Corwin Latimer
(line 1) Dancer Choreographer Instructor Singer/Songwriter
(line 2) Ballet-Modern-Urban
corwinlatimer00@quillpost.example
410-582-7146

Requirements
Nice to have

• Open to an all typography card.
Should not have
• No logo; just name: Corwin Latimer
Corwin is a guy (in case you were wondering :D )
Please no ballet/pointe shoes in design

```html
<!DOCTYPE html>
<html lang="en">
<head>
<meta charset="utf-8">
<title>Corwin Latimer — Business Card</title>
<link rel="stylesheet" href="https://fonts.googleapis.com/css2?family=Federo&display=swap">
<style>
  :root {
    --page-bg: #e6e6e6;
    --card-black: #1b1b1b;
    --band-light: #5e5e5e;
    --band-mid: #4a4a4a;
    --band-dark: #2c2c2c;
    --ring: #1a1a1a;
    --photo-light: #4f6fb8;
    --photo-dark: #2a4488;
    --text-light: #cfcfcf;
    --rule: #b5b5b5;
  }
  * { margin: 0; padding: 0; box-sizing: border-box; }
  html, body {
    width: 1200px;
    height: 1000px;
    overflow: hidden;
    background: var(--page-bg);
  }
  .business-card {
    position: absolute;
    left: 110px;
    top: 224px;
    width: 980px;
    height: 552px;
    background: var(--card-black);
    overflow: hidden;
    box-shadow: 0 8px 24px rgba(0,0,0,0.25);
  }
  .info-band {
    position: absolute;
    left: 0;
    top: 129px;
    width: 100%;
    height: 303px;
    background: linear-gradient(90deg, var(--band-dark) 0%, var(--band-light) 30%, var(--band-mid) 70%, var(--band-dark) 100%);
  }
  .portrait-frame {
    position: absolute;
    left: 74px;
    top: 48px;
    width: 246px;
    height: 246px;
    border-radius: 50%;
    background: var(--ring);
  }
  .portrait-photo {
    position: absolute;
    left: 22px;
    top: 22px;
    width: 202px;
    height: 202px;
    border-radius: 50%;
    background: linear-gradient(180deg, var(--photo-light) 0%, var(--photo-dark) 100%);
  }
  .card-details {
    position: absolute;
    right: 101px;
    top: 0;
    width: 660px;
    height: 100%;
    text-align: right;
    font-family: "Federo", sans-serif;
    color: var(--text-light);
  }
  .card-name {
    position: absolute;
    right: 0;
    top: 150px;
    font-size: 64px;
    line-height: 1;
    letter-spacing: 5px;
    font-weight: 400;
    white-space: nowrap;
  }
  .name-rule {
    position: absolute;
    right: 0;
    top: 228px;
    width: 510px;
    height: 2px;
    background: var(--rule);
  }
  .card-line {
    position: absolute;
    right: 0;
    font-size: 28px;
    line-height: 1;
    white-space: nowrap;
  }
  .card-roles { top: 258px; }
  .card-styles { top: 300px; }
  .card-email { top: 338px; font-size: 26px; }
  .card-phone { top: 372px; font-size: 30px; letter-spacing: 1px; }
</style>
</head>
<body>
  <div class="business-card">
    <div class="info-band"></div>
    <div class="portrait-frame">
      <div class="portrait-photo" role="img" aria-label="Photo of the dancer in an extended pose"></div>
    </div>
    <div class="card-details">
      <h1 class="card-name">Corwin Latimer</h1>
      <div class="name-rule"></div>
      <p class="card-line card-roles">Dancer Choreographer Instructor Singer/Songwriter</p>
      <p class="card-line card-styles">Ballet-Modern-Urban</p>
      <p class="card-line card-email">corwinlatimer00@quillpost.example</p>
      <p class="card-line card-phone">410-582-7146</p>
    </div>
  </div>
</body>
</html>
```